High-End Print/Digital Ad for Unique Luxury Travel Company Required

Objective:
Design a compelling and visually striking advertisement that highlights our company’s unmatched luxury travel experiences. The ad should elevate our brand image, spark curiosity, and drive prospective clients to contact us.
Target Audience:
• Affluent individuals seeking extraordinary, tailor-made travel experiences
• Affluent, luxury, high-net-worth individuals looking for value, expertise, and white-glove service
• Professionals or retirees who appreciate unique, thoughtfully curated travel over mainstream tourism
Key Messages to Communicate:
• One-of-a-kind luxury travel: Once-in-a-lifetime experiences that are curated with creativity and meticulous attention to detail
• Exceptional service: White-glove, personalized planning from start to finish
• 38 years’ travel experience – expert knowledge of destinations, modes of travel, premium accommodations and well-established, meaningful industry connections.
• Highly trusted: Cruise line executives often say, “No one does what you do.”
Tone and Style:
• Elegant, luxurious, sophisticated
• Eye-catching, polished, and modern
• Professional but warm—conveys trust and credibility
• High-impact visuals (full-bleed imagery, custom graphics, or high-end photography)
Deliverables:
• One full-page print ad and digital ad
• Ready-to-print, high-resolution file + working file (PSD, AI, etc.)
Optional: Social media-optimized version or short motion-graphic variation (if designer offers it)
Inspiration & Visual Style Suggestions:
• Think Velvet Voyager, Brimley Hart Wanderer, Seven Lanterns, or Oriel Retreats ad styles
• Large, emotive imagery with elegant typography
• Clean layout that speaks luxury, clarity, and trust
Copy Direction (draft):
For those who’ve explored the world—and crave something beyond the ordinary.
Each journey is a masterfully curated experience, rich in detail, seamless in execution, and unforgettable in every way.
Founded in 1997, Tidewell Journeys is a unique travel company specializing in cruising, all-inclusive luxury properties, and tours world-wide for individuals, groups, and incentives.
We offer an exceptional range of services designed to ensure every journey is flawlessly executed and truly unforgettable.
Let us help you plan your next extraordinary adventure.
Note: You may refine the copy slightly based on layout or format needs.
Other Resources for References:
1. Website - www.tidewelljourneys.example

```html
<!DOCTYPE html>
<html lang="en">
<head>
<meta charset="utf-8">
<title>Tidewell Journeys — Luxury Reimagined</title>
<link href="https://fonts.googleapis.com/css2?family=Poppins:wght@300;400;500;600;700;800&display=swap" rel="stylesheet">
<style>
  :root {
    --white: #ffffff;
    --yellow: #f6ec12;
    --sky-blue: #22a6e8;
    --sky-top: #2a6d95;
    --sky-mid: #3e7fa6;
    --rock: #6a5448;
    --peak: #c9623a;
    --forest: #1f4a34;
    --lake: #12506a;
    --lake-deep: #0d3e58;
    --divider: rgba(255,255,255,0.35);
  }
  * { margin: 0; padding: 0; box-sizing: border-box; }
  html, body { width: 910px; height: 1200px; overflow: hidden; background: #e4e4e4; }
  .ad {
    position: relative;
    width: 910px;
    height: 1200px;
    overflow: hidden;
    font-family: "Poppins", sans-serif;
    color: var(--white);
  }
  .ad__scenery {
    position: absolute;
    inset: 0;
    background:
      linear-gradient(180deg,
        var(--sky-top) 0%,
        var(--sky-mid) 30%,
        #4c86a8 40%,
        var(--peak) 47%,
        var(--rock) 55%,
        var(--forest) 66%,
        var(--lake) 78%,
        var(--lake-deep) 100%);
  }
  .abs { position: absolute; }
  .headline {
    left: 0; width: 910px; top: 64px;
    text-align: center;
    font-weight: 600;
    font-size: 194px;
    line-height: 1;
    letter-spacing: -8px;
  }
  .headline__sub {
    left: 0; width: 910px; top: 232px;
    text-align: center;
    font-weight: 600;
    font-size: 84px;
    line-height: 1;
    letter-spacing: -3px;
    color: var(--yellow);
  }
  .tagline {
    left: 0; width: 910px; top: 326px;
    text-align: center;
  }
  .tagline__lead {
    display: block;
    font-weight: 700; font-size: 33px; line-height: 44px;
    letter-spacing: -0.8px;
  }
  .tagline__rest {
    display: block;
    font-weight: 300; font-size: 29px; line-height: 40px;
  }
  .reputation {
    left: 81px; top: 562px;
    font-weight: 800;
    font-size: 62px;
    line-height: 57px;
    letter-spacing: -1.8px;
    color: var(--sky-blue);
    text-transform: uppercase;
  }
  .quote { left: 80px; top: 684px; width: 320px; height: 130px; }
  .quote__mark {
    position: absolute;
    font-family: Georgia, serif;
    font-weight: 700;
    font-size: 58px;
    line-height: 1;
    color: var(--sky-blue);
  }
  .quote__mark--open { left: 0; top: 6px; }
  .quote__mark--close { left: 244px; top: 42px; }
  .quote__text {
    position: absolute; left: 58px; top: 0;
    font-weight: 600; font-size: 26px; line-height: 33px;
    white-space: nowrap;
  }
  .quote__author {
    position: absolute; left: 51px; top: 70px;
    font-weight: 600; font-size: 25px; line-height: 34px;
    white-space: nowrap;
  }
  .quote__role {
    position: absolute; left: 71px; top: 104px;
    font-weight: 400; font-size: 18px; line-height: 22px; letter-spacing: 4px;
    color: var(--yellow);
  }
  .feature { top: 865px; width: 200px; }
  .feature__title {
    font-weight: 700; font-size: 22px; line-height: 29px;
    color: var(--yellow);
  }
  .feature__body {
    margin-top: 16px;
    font-weight: 400; font-size: 15px; line-height: 18.5px;
  }
  .feature--bespoke { left: 78px; }
  .feature--service { left: 309px; }
  .feature--cta { left: 528px; width: 262px; }
  .divider {
    top: 863px; width: 1px; height: 140px;
    background: var(--divider);
  }
  .divider--one { left: 290px; }
  .divider--two { left: 507px; }
  .contact {
    left: 539px; top: 1021px;
    font-style: normal;
    font-weight: 600; font-size: 20px; line-height: 27px;
    white-space: nowrap;
  }
  .brand {
    left: 86px; top: 1058px;
    font-weight: 400; font-size: 34px; line-height: 44px;
    letter-spacing: 0.5px;
    white-space: nowrap;
  }
</style>
</head>
<body>
  <main class="ad">
    <div class="ad__scenery" role="img" aria-label="Photograph of a turquoise mountain lake at sunrise, with sunlit orange rocky peaks, a dense pine forest along the shore, and a cloud-streaked blue sky above"></div>

    <h1 class="abs headline">LUXURY</h1>
    <p class="abs headline__sub">REIMAGINED</p>

    <p class="abs tagline">
      <span class="tagline__lead">Once-in-a-lifetime journeys, designed with</span>
      <span class="tagline__rest">vision, trust, and timeless detail.</span>
    </p>

    <h2 class="abs reputation">Unrivaled<br>Reputation</h2>

    <blockquote class="abs quote">
      <span class="quote__mark quote__mark--open">&ldquo;</span>
      <p class="quote__text">No one does<br>what you do.</p>
      <span class="quote__mark quote__mark--close">&rdquo;</span>
      <p class="quote__author">- Cruise Line</p>
      <p class="quote__role">EXECUTIVE</p>
    </blockquote>

    <section class="abs feature feature--bespoke">
      <h3 class="feature__title">Bespoke<br>Experiences</h3>
      <p class="feature__body">Impeccably curated adventures crafted with creativity and care.</p>
    </section>
    <div class="abs divider divider--one"></div>
    <section class="abs feature feature--service">
      <h3 class="feature__title">White-Glove<br>Service</h3>
      <p class="feature__body">From first idea to final return, every detail is flawlessly handled.</p>
    </section>
    <div class="abs divider divider--two"></div>
    <section class="abs feature feature--cta">
      <h3 class="feature__title">Let us create your next<br>unforgettable escape.</h3>
      <p class="feature__body">38 years of unmatched insight,<br>global connections, and<br>premium access.</p>
    </section>

    <p class="abs brand">Tidewell Journeys</p>

    <address class="abs contact">
      800.555.0142<br>
      TidewellJourneys.example<br>
      www.tidewelljourneys.example
    </address>
  </main>
</body>
</html>
```